Crumb Joy pastry business card design

I need a logo and a business card design for my baking business, "Crumb Joy". I daily bake French pastries from scratch using high quality ingredients and directly cater to local customers. My product is very authentic but sold at a casual setting . I'm looking for a simple, cute, stylish yet earthy design. Like this kind of feel:
http://clipvista.example/71946302
Target Market(s)
Metropolitan food conscious consumers in their 20-40s
Industry/Entity Type
Business
Requirements
Must have
- Soft pastel colors or other types of color schemes that would remind French pastries.
email: welovecrumbles@mailnest.example
twitter@bitemesf
www.crumbjoyla.example
Nice to have
Should not have
- pictures of pastries - sketches are ok.

```html
<!DOCTYPE html>
<html lang="en">
<head>
<meta charset="utf-8">
<title>Crumb Joy – Business Card</title>
<link rel="stylesheet" href="https://fonts.googleapis.com/css2?family=Josefin+Sans:wght@400;600&family=Patrick+Hand+SC&display=swap">
<style>
  :root {
    --paper: #ffffff;
    --ink: #0a0a0a;
    --peach: #ffb088;
    --sky: #8cb3e3;
    --stripe-blue: #9ca4e2;
    --stripe-rose: #f4a2a2;
  }
  html, body {
    margin: 0;
    padding: 0;
    overflow: hidden;
    background: var(--paper);
  }
  .card {
    position: relative;
    width: 1200px;
    height: 689px;
    background: var(--paper);
    overflow: hidden;
  }
  .brand-name {
    position: absolute;
    left: 24px;
    top: 90px;
    margin: 0;
    font-family: "Josefin Sans", sans-serif;
    font-weight: 600;
    font-size: 150px;
    line-height: 170px;
    color: var(--peach);
    letter-spacing: -2px;
  }
  .brand-name span { display: block; }
  .contact-list {
    position: absolute;
    left: 552px;
    top: 112px;
    margin: 0;
    padding: 0;
    list-style: none;
    font-family: "Josefin Sans", sans-serif;
    font-weight: 400;
    font-size: 98px;
    line-height: 84px;
    color: var(--ink);
    letter-spacing: -1px;
    text-transform: uppercase;
  }
  .tagline {
    position: absolute;
    left: 556px;
    top: 572px;
    margin: 0;
    font-family: "Patrick Hand SC", cursive;
    font-size: 62px;
    line-height: 1;
    color: var(--sky);
    letter-spacing: 1px;
  }
  .edge-stripes {
    position: absolute;
    top: 0;
    right: 0;
    width: 60px;
    height: 689px;
  }
</style>
</head>
<body>
  <main class="card">
    <h1 class="brand-name"><span>Crumb</span><span>Joy</span></h1>

    <ul class="contact-list">
      <li>Name</li>
      <li>Phone</li>
      <li>Address</li>
      <li>Website</li>
    </ul>

    <p class="tagline">French pastries</p>

    <svg class="edge-stripes" viewBox="0 0 60 689" aria-hidden="true">
      <rect x="3" y="0" width="13" height="689" fill="var(--stripe-blue)"/>
      <rect x="34" y="0" width="13" height="689" fill="var(--stripe-rose)"/>
    </svg>
  </main>
</body>
</html>
```